Create modern and sleek business card for luxury real estate company

We're a "boutique" real estate office looking for a design that gets across a highly modern luxury brand. Blacks and whites are probably the best colors unless we try a silver foil for the logo. I've attached a version of our current logo here. I'd like to swap out the current font on there with Gotham Light Regular.

I'm looking to have one side of the card have the logo with the space for our agents info on the other side.

Target Market(s)

Young professionals in a "luxury" headspace

Industry/Entity Type

Real estate

Contact Information for Business Card

A place for agent name, cell number, website. The slogan "Quietly Redefining Fine Living".

Font styles to use
Other font styles liked:
• Gotham Regular

Colors

Designer to choose only greyscale colors for use in the design.

Requirements
Must have
• Matte black as the background color. Clean lines and use of contrast. A specific design aspect that will use silver foil.
Nice to have
• Up in the air on integrating a QR code
Should not have
• Any houses or other real estate related design (ex: a clip art house)

```html
<!DOCTYPE html>
<html lang="en">
<head>
<meta charset="utf-8">
<title>Meridian Realty — Business Card</title>
<link href="https://fonts.googleapis.com/css2?family=Montserrat:wght@300;400;500;600&display=swap" rel="stylesheet">
<style>
  :root {
    --stage: #3b3b3b;
    --matte-black: #0b0b0b;
    --quilt-dark: #060606;
    --quilt-mid: #1a1a1a;
    --paper: #f7f7f7;
    --ink: #111111;
    --silver: #d6d6d6;
    --silver-light: #f2f2f2;
    --silver-dark: #8a8a8a;
    --ghost: #e6e6e6;
  }
  * { margin: 0; padding: 0; box-sizing: border-box; }
  html, body { width: 1200px; height: 1165px; overflow: hidden; }
  body {
    background: var(--stage);
    font-family: "Montserrat", sans-serif;
    position: relative;
  }
  .card {
    position: absolute;
    width: 771px;
    height: 440px;
    overflow: hidden;
    box-shadow: 0 14px 30px rgba(0,0,0,.45);
  }
  .card--front { left: 196px; top: 88px; background: var(--paper); }
  .card--back { left: 195px; top: 592px; }

  .quilt {
    position: absolute;
    background: radial-gradient(ellipse at 50% 30%, var(--quilt-mid), var(--quilt-dark) 75%);
  }
  .card--front .quilt { left: 0; top: 0; width: 288px; height: 440px; }
  .card--back .quilt { inset: 0; }

  .foil-band {
    position: absolute;
    background: linear-gradient(90deg, var(--silver-dark), var(--silver-light) 45%, var(--silver) 60%, var(--silver-dark));
  }
  .foil-band--vertical-thin { left: 288px; top: 0; width: 4px; height: 440px;
    background: linear-gradient(180deg, var(--silver-light), var(--silver-dark)); }
  .divider-black { position: absolute; left: 292px; top: 0; width: 7px; height: 440px; background: var(--matte-black); }
  .foil-band--vertical { left: 299px; top: 0; width: 22px; height: 440px;
    background: linear-gradient(180deg, var(--silver-light), var(--silver) 40%, var(--silver-dark) 80%, var(--silver)); }

  .mark {
    position: absolute;
    border: 3px solid var(--silver);
    border-radius: 50%;
    display: flex; align-items: center; justify-content: center;
    color: var(--silver);
    font-weight: 400;
    letter-spacing: 2px;
  }
  .mark--front { left: 52px; top: 139px; width: 166px; height: 166px; font-size: 20px; }

  .agent-name {
    position: absolute; left: 375px; top: 52px;
    font-size: 48px; font-weight: 600; color: var(--ink); letter-spacing: -0.5px;
    line-height: 1.2;
  }
  .agent-rule { position: absolute; left: 376px; top: 118px; width: 112px; height: 2px; background: var(--ink); }
  .agent-title {
    position: absolute; left: 504px; top: 112px;
    font-size: 12px; font-weight: 500; letter-spacing: 2.6px; color: var(--ink); line-height: 1;
  }
  .slogan {
    position: absolute; left: 375px; top: 139px;
    font-size: 19px; font-weight: 600; color: var(--ink);
  }
  .contacts { position: absolute; left: 372px; top: 285px; list-style: none; }
  .contacts li {
    display: flex; align-items: center; gap: 13px;
    height: 37px; font-size: 18px; font-weight: 500; color: var(--ink);
  }
  .contacts svg { width: 25px; height: 25px; flex: none; }

  .ghost-ring {
    position: absolute; left: 540px; top: 225px; width: 250px; height: 250px;
    border: 6px solid var(--ghost); border-radius: 50%;
  }

  .mark--back { left: 182px; top: 147px; width: 145px; height: 145px; }
  .wordmark-block {
    position: absolute; left: 347px; top: 166px; width: 243px;
    text-align: center; color: var(--silver);
  }
  .wordmark {
    font-size: 42px; font-weight: 300; letter-spacing: 1px; line-height: 1;
  }
  .wordmark-rule { height: 3px; background: var(--silver); margin: 10px 0 12px; }

  .foil-line { position: absolute; left: 0; top: 408px; width: 771px; height: 3px;
    background: linear-gradient(90deg, var(--silver-dark), var(--silver-light) 50%, var(--silver-dark)); }
  .foil-band--bottom { left: 0; top: 418px; width: 771px; height: 22px; }
</style>
</head>
<body>

<section class="card card--front" aria-label="Business card, agent side">
  <div class="quilt" role="img" aria-label="Black quilted diamond texture panel"></div>
  <div class="foil-band foil-band--vertical-thin"></div>
  <div class="divider-black"></div>
  <div class="foil-band foil-band--vertical"></div>
  <div class="mark mark--front">MERIDIAN</div>

  <div class="ghost-ring" aria-hidden="true"></div>

  <h1 class="agent-name">Dorian Vale</h1>
  <div class="agent-rule"></div>
  <p class="agent-title">DIRECTOR MANAGER</p>
  <p class="slogan">Quietly Redefining Fine Living</p>

  <ul class="contacts">
    <li>
      <svg viewBox="0 0 24 24" aria-hidden="true"><circle cx="12" cy="12" r="12" fill="#111"/><path d="M8.2 6.5l2 .2.9 2.6-1.3 1.1a7 7 0 0 0 3.8 3.8l1.1-1.3 2.6.9.2 2c-.5 1-1.7 1.6-2.9 1.2A10 10 0 0 1 7 9.4c-.4-1.2.2-2.4 1.2-2.9z" fill="#fff"/></svg>
      <span>5550142873</span>
    </li>
    <li>
      <svg viewBox="0 0 24 24" aria-hidden="true"><circle cx="12" cy="12" r="12" fill="#111"/><g fill="none" stroke="#bbb" stroke-width="1"><circle cx="12" cy="12" r="6.5"/><ellipse cx="12" cy="12" rx="3" ry="6.5"/><path d="M5.5 12h13M6.5 8.5h11M6.5 15.5h11"/></g></svg>
      <span>www.meridianhomes.com</span>
    </li>
    <li>
      <svg viewBox="0 0 24 24" aria-hidden="true"><circle cx="12" cy="12" r="12" fill="#111"/><path d="M12 5.5a4.5 4.5 0 0 0-4.5 4.5c0 3.3 4.5 8.5 4.5 8.5s4.5-5.2 4.5-8.5A4.5 4.5 0 0 0 12 5.5z" fill="#fff"/><circle cx="12" cy="10" r="1.7" fill="#111"/></svg>
      <span>Street no 9 Riverton</span>
    </li>
  </ul>
</section>

<section class="card card--back" aria-label="Business card, brand side">
  <div class="quilt" role="img" aria-label="Black quilted diamond texture background"></div>
  <div class="mark mark--back" aria-hidden="true"></div>
  <div class="wordmark-block">
    <p class="wordmark">MERIDIAN</p>
    <div class="wordmark-rule"></div>
    <p class="wordmark">REALTY</p>
  </div>
  <div class="foil-line"></div>
  <div class="foil-band foil-band--bottom"></div>
</section>

</body>
</html>
```